Digital menu Skydiving company

Design Digital menu/pricelist for our company. It can have dynamic components. We are also looking for a Graphic design for all our projects. Our main goals are to look clean/sharp and professional. Information is in psd file

3 packages Amber Plunge, Harbor Voyage, And Thunder Journey. then we have addons and merchandise

Colors
0293ce
34a7d8
ffffff
fbee3f
3377b5
000000
f37122
ec1f27
e34197

Requirements
Must have
• Sorry If I couldn't get my vision across better, Please see really rough design idea attached. one large picture section that rotates through 3 or 4 pictures. then all the information down the bottom and on right (see menu pricelist attached)

```html
<!DOCTYPE html>
<html lang="en">
<head>
<meta charset="utf-8">
<title>Halcyon Skydive – Digital Price Menu</title>
<link href="https://fonts.googleapis.com/css2?family=Montserrat:wght@500;600;700;800&display=swap" rel="stylesheet">
<style>
:root{
  --sky:#0293ce;
  --sky-light:#34a7d8;
  --pale:#7cc6ea;
  --pale-soft:#a6d9f1;
  --mid:#1e8fcf;
  --mid-soft:#3aa3dc;
  --navy:#0f4c9c;
  --navy-soft:#2a63b0;
  --ink:#1f2a3b;
  --title:#123f86;
  --white:#ffffff;
  --stage:#f2f3f5;
}
*{box-sizing:border-box;margin:0;padding:0}
html,body{width:1200px;height:1000px;overflow:hidden}
body{background:var(--stage);font-family:"Montserrat",Arial,sans-serif;position:relative}

.menu-screen{position:absolute;width:585px;height:370px;background:var(--white);overflow:hidden;box-shadow:0 14px 22px rgba(0,0,0,.12)}
.menu-screen--amber{left:15px;top:328px;transform:scale(.983);transform-origin:0 0}
.menu-screen--harbor{left:605px;top:95px}
.menu-screen--thunder{left:605px;top:505px}

.hero{position:absolute;left:0;top:0;width:585px;height:158px}
.hero-art{position:absolute;inset:0}
.brand{position:absolute;left:16px;top:20px;display:flex;align-items:center;gap:6px;color:var(--title);font-weight:800;font-size:11px;letter-spacing:.5px;line-height:1}
.brand-dot{width:9px;height:9px;border-radius:50%;background:var(--sky)}
.hero-title{position:absolute;left:18px;top:86px;color:var(--white);font-weight:700;font-size:25px;line-height:24px;letter-spacing:.3px}
.hero-title::after{content:"";display:block;width:46px;height:4px;background:var(--navy);margin-top:7px}

.addons{position:absolute;left:387px;top:5px;width:185px;height:146px;background:var(--white)}
.addons-head{height:36px;background:var(--ink);color:var(--white);font-weight:700;font-size:14px;display:flex;align-items:center;justify-content:center}
.addons-list{list-style:none;padding:6px 6px 0 8px}
.addons-list li{display:flex;justify-content:space-between;font-size:7px;font-weight:700;color:var(--ink);text-transform:uppercase;line-height:13px}
.addons-list li.sub{padding-left:22px;text-transform:none;font-weight:600;line-height:10px}
.chev{color:var(--sky);margin-right:4px;font-weight:800}

.section-title{position:absolute;left:0;width:585px;top:160px;text-align:center;color:var(--title);font-weight:800;font-size:21px;letter-spacing:.2px}

.package{position:absolute;top:187px;width:185px;height:177px;background:var(--ink);color:var(--white)}
.package--amber{left:5px}
.package--harbor{left:196px}
.package--thunder{left:387px}
.package::after{content:"";position:absolute;left:0;right:0;bottom:-3px;height:3px}
.package-head{height:35px;display:flex;flex-direction:column;justify-content:center;align-items:center;font-weight:700;font-size:13px;line-height:14px;text-align:center}
.package-tag{height:15px;font-size:8px;font-weight:500;display:flex;align-items:center;justify-content:center;letter-spacing:.3px}
.package--amber .package-head{background:var(--pale)}
.package--amber .package-tag{background:var(--pale-soft)}
.package--amber::after{background:var(--pale)}
.package--harbor .package-head{background:var(--mid)}
.package--harbor .package-tag{background:var(--mid-soft)}
.package--harbor::after{background:var(--mid)}
.package--thunder .package-head{background:var(--navy)}
.package--thunder .package-tag{background:var(--navy-soft)}
.package--thunder::after{background:var(--navy)}

.features{list-style:none;padding:6px 6px 0 8px}
.features li{display:flex;justify-content:space-between;font-size:6.6px;font-weight:700;text-transform:uppercase;line-height:14px}
.price{position:absolute;left:50%;transform:translateX(-50%);width:66px;height:19px;border-radius:10px;color:var(--white);font-weight:700;font-size:15px;display:flex;align-items:center;justify-content:center}
.package--amber .price{top:92px;background:var(--pale)}
.package--harbor .price{top:148px;background:var(--mid)}
.package--thunder .price{top:148px;background:var(--navy)}

.extras{position:absolute;left:12px;top:121px;width:163px;height:50px;border:1px solid var(--pale);display:flex}
.extras-label{width:12px;background:var(--pale);color:var(--ink);font-size:7px;font-weight:800;writing-mode:vertical-rl;transform:rotate(180deg);text-align:center}
.extras-list{list-style:none;flex:1;padding:1px 5px 0 6px}
.extras-list li{display:flex;font-size:6.6px;font-weight:500;line-height:9.4px}
.extras-list .leader{flex:1;border-bottom:1px dotted rgba(255,255,255,.7);margin:0 2px 2px}
</style>
</head>
<body>

<section class="menu-screen menu-screen--amber">
  <div class="hero">
    <svg class="hero-art" width="585" height="158" viewBox="0 0 585 158">
      <defs>
        <linearGradient id="band-a" x1="0" y1="1" x2="1" y2="0"><stop offset="0" stop-color="#1c8cc9"/><stop offset="1" stop-color="#0f6fb3"/></linearGradient>
        <linearGradient id="sky-a" x1="0" y1="0" x2="0" y2="1"><stop offset="0" stop-color="#2f79c0"/><stop offset=".6" stop-color="#7fb6de"/><stop offset="1" stop-color="#6b7f8f"/></linearGradient>
      </defs>
      <polygon points="0,92 175,0 585,0 585,158 0,158" fill="url(#band-a)"/>
      <g role="img" aria-label="Photo: tandem skydivers in freefall above a desert canyon">
        <polygon points="210,0 400,0 400,158 150,158" fill="url(#sky-a)"/>
      </g>
      <polygon points="175,0 205,0 130,45 108,35" fill="#4fb6e6" opacity=".8"/>
      <polygon points="120,70 150,55 90,158 62,158" fill="#3aa3dc" opacity=".6"/>
    </svg>
    <div class="brand"><span class="brand-dot"></span>HALCYON SKYDIVE</div>
    <h1 class="hero-title">AMBER<br>PLUNGE</h1>
    <div class="addons">
      <div class="addons-head">ADD ONS</div>
      <ul class="addons-list">
        <li><span><span class="chev">»</span>Photos</span><span>$99</span></li>
        <li><span><span class="chev">»</span>Videos</span><span>$99</span></li>
        <li><span><span class="chev">»</span>Extreme Extras</span><span>$50</span></li>
        <li><span><span class="chev">»</span>Las Vegas Transport</span><span>$119+</span></li>
        <li><span><span class="chev">»</span>Phoenix Transport</span><span>$259</span></li>
        <li><span><span class="chev">»</span>Group Specials</span><span></span></li>
        <li class="sub"><span>4 – 7</span><span>$25 off / person</span></li>
        <li class="sub"><span>8+</span><span>$35 off / person</span></li>
      </ul>
    </div>
  </div>
  <h2 class="section-title">PACKAGES &amp; PRICES</h2>
  <article class="package package--amber">
    <div class="package-head">AMBER PLUNGE<br>16,000FT</div>
    <div class="package-tag">THE SKYDIVE IS NAKED, NOT YOU...</div>
    <ul class="features">
      <li><span><span class="chev">»</span>Tandem skydive from 16,000ft MSL</span></li>
      <li><span><span class="chev">»</span>Certificate of achievement</span></li>
    </ul>
    <div class="price">$329</div>
    <div class="extras"><div class="extras-label">EXTRAS</div>
      <ul class="extras-list">
        <li>T-Shirt Short Sleeve<span class="leader"></span>$20</li>
        <li>T-Shirt Long Sleeve<span class="leader"></span>$28</li>
        <li>Sweat Shirts<span class="leader"></span>$30</li>
        <li>Hoodies<span class="leader"></span>$38</li>
        <li>Goggles from<span class="leader"></span>$12</li>
      </ul></div>
  </article>
  <article class="package package--harbor">
    <div class="package-head">HARBOR VOYAGE<br>16,000FT</div>
    <div class="package-tag">SKYDIVE &amp; SHARE THE MEMORIES...</div>
    <ul class="features">
      <li><span><span class="chev">»</span>Tandem skydive from 16,000ft MSL</span></li>
      <li><span><span class="chev">»</span>Photos</span></li>
      <li><span><span class="chev">»</span>Videos</span></li>
      <li><span><span class="chev">»</span>Certificate of achievement</span></li>
    </ul>
    <div class="price">$459</div>
  </article>
  <article class="package package--thunder">
    <div class="package-head">THUNDER JOURNEY<br>16,000FT</div>
    <div class="package-tag">FOR THE THRILL SEEKER...</div>
    <ul class="features">
      <li><span><span class="chev">»</span>Tandem skydive from 16,000ft MSL</span><span>$319</span></li>
      <li><span><span class="chev">»</span>Photos</span><span>$99</span></li>
      <li><span><span class="chev">»</span>Videos</span><span>$99</span></li>
      <li><span><span class="chev">»</span>Extreme extras</span><span>$50</span></li>
      <li><span><span class="chev">»</span>Halcyon Skydive T-shirt</span></li>
      <li><span><span class="chev">»</span>Certificate of achievement</span></li>
    </ul>
    <div class="price">$499</div>
  </article>
</section>

<section class="menu-screen menu-screen--harbor">
  <div class="hero">
    <svg class="hero-art" width="585" height="158" viewBox="0 0 585 158">
      <defs>
        <linearGradient id="band-h" x1="0" y1="1" x2="1" y2="0"><stop offset="0" stop-color="#1c8cc9"/><stop offset="1" stop-color="#0f6fb3"/></linearGradient>
        <linearGradient id="photo-h" x1="0" y1="0" x2="1" y2="1"><stop offset="0" stop-color="#c9d6e0"/><stop offset=".5" stop-color="#3d7fc4"/><stop offset="1" stop-color="#1b3a6b"/></linearGradient>
      </defs>
      <polygon points="0,92 175,0 585,0 585,158 0,158" fill="url(#band-h)"/>
      <g role="img" aria-label="Photo: excited tandem skydiver with goggles beside an instructor">
        <polygon points="210,0 400,0 400,158 150,158" fill="url(#photo-h)"/>
      </g>
      <polygon points="175,0 205,0 130,45 108,35" fill="#4fb6e6" opacity=".8"/>
      <polygon points="120,70 150,55 90,158 62,158" fill="#3aa3dc" opacity=".6"/>
    </svg>
    <div class="brand"><span class="brand-dot"></span>HALCYON SKYDIVE</div>
    <h1 class="hero-title">HARBOR<br>VOYAGE</h1>
    <div class="addons">
      <div class="addons-head">ADD ONS</div>
      <ul class="addons-list">
        <li><span><span class="chev">»</span>Photos</span><span>$99</span></li>
        <li><span><span class="chev">»</span>Videos</span><span>$99</span></li>
        <li><span><span class="chev">»</span>Extreme Extras</span><span>$50</span></li>
        <li><span><span class="chev">»</span>Las Vegas Transport</span><span>$119+</span></li>
        <li><span><span class="chev">»</span>Phoenix Transport</span><span>$259</span></li>
        <li><span><span class="chev">»</span>Group Specials</span><span></span></li>
        <li class="sub"><span>4 – 7</span><span>$25 off / person</span></li>
        <li class="sub"><span>8+</span><span>$35 off / person</span></li>
      </ul>
    </div>
  </div>
  <h2 class="section-title">PACKAGES &amp; PRICES</h2>
  <article class="package package--amber">
    <div class="package-head">AMBER PLUNGE<br>16,000FT</div>
    <div class="package-tag">THE SKYDIVE IS NAKED, NOT YOU...</div>
    <ul class="features">
      <li><span><span class="chev">»</span>Tandem skydive from 16,000ft MSL</span></li>
      <li><span><span class="chev">»</span>Certificate of achievement</span></li>
    </ul>
    <div class="price">$329</div>
    <div class="extras"><div class="extras-label">EXTRAS</div>
      <ul class="extras-list">
        <li>T-Shirt Short Sleeve<span class="leader"></span>$20</li>
        <li>T-Shirt Long Sleeve<span class="leader"></span>$28</li>
        <li>Sweat Shirts<span class="leader"></span>$30</li>
        <li>Hoodies<span class="leader"></span>$38</li>
        <li>Goggles from<span class="leader"></span>$12</li>
      </ul></div>
  </article>
  <article class="package package--harbor">
    <div class="package-head">HARBOR VOYAGE<br>16,000FT</div>
    <div class="package-tag">SKYDIVE &amp; SHARE THE MEMORIES...</div>
    <ul class="features">
      <li><span><span class="chev">»</span>Tandem skydive from 16,000ft MSL</span></li>
      <li><span><span class="chev">»</span>Photos</span></li>
      <li><span><span class="chev">»</span>Videos</span></li>
      <li><span><span class="chev">»</span>Certificate of achievement</span></li>
    </ul>
    <div class="price">$459</div>
  </article>
  <article class="package package--thunder">
    <div class="package-head">THUNDER JOURNEY<br>16,000FT</div>
    <div class="package-tag">FOR THE THRILL SEEKER...</div>
    <ul class="features">
      <li><span><span class="chev">»</span>Tandem skydive from 16,000ft MSL</span><span>$319</span></li>
      <li><span><span class="chev">»</span>Photos</span><span>$99</span></li>
      <li><span><span class="chev">»</span>Videos</span><span>$99</span></li>
      <li><span><span class="chev">»</span>Extreme extras</span><span>$50</span></li>
      <li><span><span class="chev">»</span>Halcyon Skydive T-shirt</span></li>
      <li><span><span class="chev">»</span>Certificate of achievement</span></li>
    </ul>
    <div class="price">$499</div>
  </article>
</section>

<section class="menu-screen menu-screen--thunder">
  <div class="hero">
    <svg class="hero-art" width="585" height="158" viewBox="0 0 585 158">
      <defs>
        <linearGradient id="band-t" x1="0" y1="1" x2="1" y2="0"><stop offset="0" stop-color="#1c8cc9"/><stop offset="1" stop-color="#0f6fb3"/></linearGradient>
        <linearGradient id="photo-t" x1="0" y1="0" x2="1" y2="1"><stop offset="0" stop-color="#dfe6ec"/><stop offset=".45" stop-color="#5a8fc6"/><stop offset="1" stop-color="#23344f"/></linearGradient>
      </defs>
      <polygon points="0,92 175,0 585,0 585,158 0,158" fill="url(#band-t)"/>
      <g role="img" aria-label="Photo: tandem pair jumping from the aircraft door">
        <polygon points="210,0 400,0 400,158 150,158" fill="url(#photo-t)"/>
      </g>
      <polygon points="175,0 205,0 130,45 108,35" fill="#4fb6e6" opacity=".8"/>
      <polygon points="120,70 150,55 90,158 62,158" fill="#3aa3dc" opacity=".6"/>
    </svg>
    <div class="brand"><span class="brand-dot"></span>HALCYON SKYDIVE</div>
    <h1 class="hero-title">THUNDER<br>JOURNEY</h1>
    <div class="addons">
      <div class="addons-head">ADD ONS</div>
      <ul class="addons-list">
        <li><span><span class="chev">»</span>Photos</span><span>$99</span></li>
        <li><span><span class="chev">»</span>Videos</span><span>$99</span></li>
        <li><span><span class="chev">»</span>Extreme Extras</span><span>$50</span></li>
        <li><span><span class="chev">»</span>Las Vegas Transport</span><span>$119+</span></li>
        <li><span><span class="chev">»</span>Phoenix Transport</span><span>$259</span></li>
        <li><span><span class="chev">»</span>Group Specials</span><span></span></li>
        <li class="sub"><span>4 – 7</span><span>$25 off / person</span></li>
        <li class="sub"><span>8+</span><span>$35 off / person</span></li>
      </ul>
    </div>
  </div>
  <h2 class="section-title">PACKAGES &amp; PRICES</h2>
  <article class="package package--amber">
    <div class="package-head">AMBER PLUNGE<br>16,000FT</div>
    <div class="package-tag">THE SKYDIVE IS NAKED, NOT YOU...</div>
    <ul class="features">
      <li><span><span class="chev">»</span>Tandem skydive from 16,000ft MSL</span></li>
      <li><span><span class="chev">»</span>Certificate of achievement</span></li>
    </ul>
    <div class="price">$329</div>
    <div class="extras"><div class="extras-label">EXTRAS</div>
      <ul class="extras-list">
        <li>T-Shirt Short Sleeve<span class="leader"></span>$20</li>
        <li>T-Shirt Long Sleeve<span class="leader"></span>$28</li>
        <li>Sweat Shirts<span class="leader"></span>$30</li>
        <li>Hoodies<span class="leader"></span>$38</li>
        <li>Goggles from<span class="leader"></span>$12</li>
      </ul></div>
  </article>
  <article class="package package--harbor">
    <div class="package-head">HARBOR VOYAGE<br>16,000FT</div>
    <div class="package-tag">SKYDIVE &amp; SHARE THE MEMORIES...</div>
    <ul class="features">
      <li><span><span class="chev">»</span>Tandem skydive from 16,000ft MSL</span></li>
      <li><span><span class="chev">»</span>Photos</span></li>
      <li><span><span class="chev">»</span>Videos</span></li>
      <li><span><span class="chev">»</span>Certificate of achievement</span></li>
    </ul>
    <div class="price">$459</div>
  </article>
  <article class="package package--thunder">
    <div class="package-head">THUNDER JOURNEY<br>16,000FT</div>
    <div class="package-tag">FOR THE THRILL SEEKER...</div>
    <ul class="features">
      <li><span><span class="chev">»</span>Tandem skydive from 16,000ft MSL</span><span>$319</span></li>
      <li><span><span class="chev">»</span>Photos</span><span>$99</span></li>
      <li><span><span class="chev">»</span>Videos</span><span>$99</span></li>
      <li><span><span class="chev">»</span>Extreme extras</span><span>$50</span></li>
      <li><span><span class="chev">»</span>Halcyon Skydive T-shirt</span></li>
      <li><span><span class="chev">»</span>Certificate of achievement</span></li>
    </ul>
    <div class="price">$499</div>
  </article>
</section>

</body>
</html>
```